Bravik = Difficult

Sto Je Treba Ni Bravik
what must be done, is not difficult...

my mom is Croatian and her name is Marela.

a Croatian expression that I came across 12 years ago is 'what must be done, is not difficult'. yes, it is counter-intuitive. but it helped me to get divorced and then to beat Stage 4 cancer. both seem impossible,

but they they had to be done, so they were not difficult.

so I have started up a new company called:
Bravik Consulting - solving difficult

I'll be working with companies that have a difficult program/project that they haven't launched yet...

I envision possibly a business card that is shaped into a "D" to represent the Croatian word of difficult.

yes, I know this is difficult - welcome to my new world - the difficult challenges are worth solving...

a nod to the red/white design of the Croatian flag would be nice.

```html
<!DOCTYPE html>
<html lang="en">
<head>
<meta charset="utf-8">
<title>Bravik Consulting – Business Card</title>
<link rel="stylesheet" href="https://fonts.googleapis.com/css2?family=Sorts+Mill+Goudy&display=swap">
<style>
  :root {
    --backdrop: #ececea;
    --card-red: #f01414;
    --card-red-light: #ff3030;
    --card-red-deep: #d80a0a;
    --card-white: #ffffff;
  }
  html, body {
    margin: 0;
    padding: 0;
    width: 1200px;
    height: 960px;
    overflow: hidden;
    background: var(--backdrop);
  }
  .canvas {
    width: 1200px;
    height: 960px;
    display: block;
  }
  .card-text {
    font-family: "Sorts Mill Goudy", "Goudy Old Style", Georgia, serif;
    fill: var(--card-white);
  }
  .holder-name { font-size: 32px; }
  .contact-line { font-size: 26px; }
  .company-name { font-size: 38px; }
  .company-word { font-size: 33px; }
  .tagline { font-size: 27px; }
</style>
</head>
<body>
<svg class="canvas" viewBox="0 0 1200 960" xmlns="http://www.w3.org/2000/svg">
  <defs>
    <radialGradient id="red-sheen" cx="0.45" cy="0.4" r="0.75">
      <stop offset="0" stop-color="var(--card-red-light)"/>
      <stop offset="0.6" stop-color="var(--card-red)"/>
      <stop offset="1" stop-color="var(--card-red-deep)"/>
    </radialGradient>
  </defs>

  <!-- Left half: contact side -->
  <g class="card-half card-contact" transform="translate(134 253)">
    <path d="M150 0 H446 V454 H150 A150 150 0 0 1 0 304 V150 A150 150 0 0 1 150 0 Z" fill="url(#red-sheen)"/>
    <text class="card-text holder-name" x="91" y="77">Dario Kovan</text>
    <g class="contact-details" text-anchor="end">
      <text class="card-text contact-line" x="360" y="197">218 Linden Avenue</text>
      <text class="card-text contact-line" x="360" y="232">Marlow, GA 30215</text>
      <text class="card-text contact-line" x="360" y="267">404-555-0172</text>
      <text class="card-text contact-line" x="360" y="301">dario@bravikconsulting.com</text>
    </g>
  </g>

  <!-- Right half: company side -->
  <g class="card-half card-company" transform="translate(604 253)">
    <path d="M0 0 H312 A150 150 0 0 1 462 150 V304 A150 150 0 0 1 312 454 H0 Z" fill="url(#red-sheen)"/>
    <text class="card-text tagline" transform="translate(54 401) rotate(-90)">solving difficult</text>
    <text class="card-text company-name" x="74" y="371">Bravik</text>
    <text class="card-text company-word" x="72" y="419">Consulting</text>
  </g>
</svg>
</body>
</html>
```